Web Design Project for a Software & Consulting Company

We have just completed a recent ArtFlock project for a new logo (see attached).
As the next stage of our rebranding we now require a website re-design to complement the new logo.
Our current site, http://www.rigsumsoft.example was built in-house and does not come across as professional as we would like. We supply software and associated services to some of the world’s largest oil companies and we need our site to reflect that level of client.
We will also be posting another design project for brochures, PowerPoint slides and other materials very soon.
We would like designs for…
Home page
Product page
• QTV
• BLZ
• FNQ
Services
News page
About Us page
Contact Us page
Page for mobile devices that gives basic company and product information
Currently the site is small but we intend to increase content to include white papers etc. this should be taken into account when designing the navigation therefore we would prefer navigation through styled text links rather than images.
Colour schemes should broadly be taken from our new logo, where the dark blue and dark green from the left and right sides of the logo are the main colours, but other, brighter accent colours can be used to highlight sections or content.
Dark Blue = C:88, M:55, Y:44, K:28
Dark Green = C:87, M:53, Y:50, K:50
NB: Don’t use the logo on our current site, make sure you use the one attached.
We would prefer the final file format to be a layered PSD.
The site should be clean and professional and communicate the following...
• That we have a great depth and breadth of knowledge about our customers’ business, enabling us to deliver the best systems and solutions.
• That we are a leading provider of cost estimation and control solutions to the oil and gas industry.
• The benefits of our software and consulting services.
• Show that we deliver outstanding customer service and value with a very high level of professionalism
• The site should have no Flash and be able to self-adjust to fit any screen size.
Things to avoid …
• Obvious and clichéd oil industry imagery, no oil rigs
• Cartoon style graphics
Our Background
We are an integrated software and consulting organization specialising in the drilling side of the oil and gas industry. Simply put our software helps companies better understand, predict and communicate the cost of drilling wells.
We have 3 software products and a consulting offering consisting of…
• QTV - Probabilistic time and cost software
• BLZ – Cost tracking and reporting software
• FNQ – (currently known as BoreMemory) – Lessons learned software
• Consulting services
Our systems are in use in over 30 countries with a broad range of clients including: GN, Solvane, Prue, Ostrelan, VONI Kelstra, SALVEM and Quorlit.
Our current site can be found at www.rigsumsoft.example
Our main competitors are
• http://www.gavondel.example/
• http://www.mirrowen.example/
• http://www.tbx.example/services/software-solutions/p1-
Our depth of drilling knowledge, quality of software and collaboration with clients differentiate us form the competition.
We strive for very high levels of customer service.
We look forward to receiving your designs!
Updates
Thanks to all the designers who have submitted a design, we appreciate the effort.
We will do our best to give individual feedback on each design but given that many are quite similar we thought we would give some general feedback first.
Nearly all the designs submitted so far have been slight variations on…
-
Top Menu
-
Scrolling Photo Banner
-
4 Columns
-
Body
-
Deep Footer
These designs are well executed but they are basically the same layout as our existing site and while there is nothing inherently wrong with this layout we would like to see some designs that are a bit more innovative and different. We don’t really want just a polished version of our current site.
Thanks again,
RST
Thanks to everyone who has submitted a design, the response has been great.
We are close to making a decision so if you are intending to submit a design please do it soon, the deadline is only a few days away.
Thanks again.
RST
Target Market(s)
Mid to high level executives
Industry/Entity Type
Oil And Gas
Look and feel

```html
<!DOCTYPE html>
<html lang="en">
<head>
<meta charset="utf-8">
<title>RigSum Software – Home</title>
<link href="https://fonts.googleapis.com/css2?family=Gelasio:wght@400;500&family=Jost:wght@500&family=PT+Sans:wght@400;700&display=swap" rel="stylesheet">
<style>
:root{
  --ink:#1f3d4a;
  --green:#2f5a3a;
  --teal:#27808e;
  --olive:#8a9a5a;
  --rule:#8f9c78;
  --body:#3a3a3a;
  --panel-a:#e9eddc;
  --panel-b:#dfe5cc;
  --slate:#565a6a;
  --slate-text:#e2e2e6;
  --accent:#9ab84a;
  --band:#3d5a4d;
  --btn:#5a5a5a;
  --red:#c33246;
  --social:#5ab3b3;
}
*{margin:0;padding:0;box-sizing:border-box}
html,body{width:1200px;height:1200px;overflow:hidden;background:#fff}
.page{position:relative;width:1080px;height:1080px;transform:scale(1.11111);transform-origin:0 0;font-family:"PT Sans",sans-serif;color:var(--body)}
.abs{position:absolute}
.brand{left:205px;top:28px;font-family:"Jost",sans-serif;font-size:30px;color:var(--ink);letter-spacing:1px;line-height:1}
.brand small{display:block;font-size:13px;letter-spacing:5px;margin-top:6px}
.brand-mark{display:inline-block;width:22px;height:22px;border-radius:50%;background:var(--teal);vertical-align:-2px;margin-right:8px}
.search{left:692px;top:64px;width:123px;height:21px;background:#e6e6e6;font-family:"Gelasio",serif;font-size:12px;color:#666;text-align:center;line-height:21px}
.buy{left:828px;top:27px;width:56px;text-align:center}
.buy svg{display:block}
.buy b{display:block;font-size:9.5px;line-height:11px;color:var(--ink);margin-top:1px;letter-spacing:.5px}
.nav{left:205px;top:97px;width:681px;height:26px;border-top:1px solid #999;border-bottom:1px solid #999;display:flex;font-family:"Gelasio",serif;font-size:14px;letter-spacing:.5px}
.nav a{text-decoration:none;color:var(--ink);text-align:center;border-right:1px solid #777;margin:2px 0;line-height:20px;height:20px}
.nav a:last-child{border-right:0}
.nav a.current{color:var(--olive)}
.banner{left:204px;top:123px;width:682px;height:180px;background:linear-gradient(#e2e2de,#d6d6d2);border:1px solid #999}
.banner h1{position:absolute;left:85px;top:30px;font-family:"Jost",sans-serif;font-weight:500;font-size:21.5px;line-height:31px;color:var(--ink);text-transform:uppercase;white-space:nowrap}
.banner h1 em{font-style:normal;color:var(--green);font-size:28px}
.arrow{position:absolute}
.intro{left:204px;top:312px;width:682px;height:338px;background:linear-gradient(135deg,var(--panel-a),var(--panel-b))}
.heading{font-family:"Gelasio",serif;font-weight:400;color:var(--teal);font-size:21px;display:flex;align-items:center;gap:4px;white-space:nowrap}
.heading::after{content:"";flex:1;border-bottom:1px solid var(--rule);margin-top:10px}
.copy{font-size:11.5px;line-height:15.3px;color:var(--body)}
.more{display:inline-block;background:var(--btn);color:#fff;font-size:13px;padding:2px 8px;border-radius:2px;box-shadow:0 1px 2px rgba(0,0,0,.3)}
.more::before{content:"\25B8 ";font-size:10px}
.papers{left:203px;top:719px;width:684px;height:168px;background:var(--slate);border:2px solid #8a8c96;border-radius:2px}
.paper{position:absolute;top:18px;width:275px;font-size:10.8px;line-height:15.2px;color:var(--slate-text)}
.dl{display:block;text-align:right;color:var(--accent);font-size:11px;margin-top:2px;padding-right:18px}
.dl::before{content:"\25B6 ";}
.divider{left:333px;top:16px;width:1px;height:140px;background:#8a8c96}
.clients{left:212px;top:926px;width:654px;height:86px;background:var(--band)}
.client-row{position:absolute;left:22px;top:8px;width:614px;height:71px;background:#fff;display:flex;align-items:center;justify-content:space-around;font-size:12px;font-weight:700;color:var(--ink)}
.footline{left:204px;top:1019px;width:682px;height:2px;background:var(--red)}
.copyright{left:226px;top:1030px;font-family:"Gelasio",serif;font-size:11.5px;color:#222}
.copyright span{display:inline-block;width:14px;height:14px;border:1.3px solid #222;border-radius:50%;font-size:10px;text-align:center;line-height:12px;margin-right:4px}
.legal{right:207px;top:1029px;font-family:"Gelasio",serif;font-size:11.5px;color:#222}
.legal a{color:#222;text-decoration:none;padding:0 5px;border-left:2px solid #222}
.legal a:first-child{border:0}
.social{left:712px;top:1056px;display:flex;gap:6px;font-size:8px;line-height:14px;color:var(--teal)}
.social span{display:flex;align-items:center;gap:2px}
.social i{display:inline-block;width:14px;height:14px;border-radius:50%;background:var(--social)}
</style>
</head>
<body>
<div class="page">
  <div class="abs brand"><span class="brand-mark"></span>RIGSUM<small>SOFTWARE</small></div>
  <div class="abs search">Search</div>
  <div class="abs buy">
    <svg width="56" height="56" viewBox="0 0 56 56"><circle cx="28" cy="28" r="27" fill="#eef0e6" stroke="#cfd4c0"/><circle cx="28" cy="28" r="24" fill="#7f9a4a"/><path d="M24 15h8v12h6L28 39 18 27h6z" fill="#fff"/></svg>
    <b>BUY NOW</b>
  </div>
  <nav class="abs nav">
    <a class="current" href="#" style="width:71px">HOME</a>
    <a href="#" style="width:86px">ABOUT US</a>
    <a href="#" style="width:89px">PRODUCT</a>
    <a href="#" style="width:93px">SERVICES</a>
    <a href="#" style="width:79px">NEWS</a>
    <a href="#" style="width:140px">MOBILE DEVICES</a>
    <a href="#" style="width:123px">CONTACT US</a>
  </nav>
  <section class="abs banner">
    <svg class="arrow" style="left:9px;top:61px" width="30" height="30"><circle cx="15" cy="15" r="14" fill="#6a6a6a" stroke="#ccc" stroke-width="2"/><path d="M18 8l-7 7 7 7" stroke="#fff" stroke-width="3" fill="none"/></svg>
    <svg class="arrow" style="left:639px;top:61px" width="30" height="30"><circle cx="15" cy="15" r="14" fill="#6a6a6a" stroke="#ccc" stroke-width="2"/><path d="M12 8l7 7-7 7" stroke="#fff" stroke-width="3" fill="none"/></svg>
    <h1>For over a decade <em>RigSum Software</em><br>has been helping companies better manage<br>the business of drilling wells.</h1>
  </section>
  <section class="abs intro">
    <h2 class="abs heading" style="left:25px;top:22px;width:612px">WELCOME</h2>
    <p class="abs copy" style="left:25px;top:77px;width:630px">Lorem ipsum dolor sit amet, consectetur adipisicing elit, sed do eiusmod tempor  incididunt ut labore et dolore magna aliqua. Ut enim ad minim veniam, quis nostrud  exercitation ullamco laboris nisi ut aliquip ex ea commodo consequat. Duis aute irure dolor in reprehenderit in voluptate velit esse cillum dolore eu fugiat nulla pariatur. Excepteur sint occaecat cupidatat non proident, sunt in culpa qui officia deserunt mollit anim id est laborum......</p>
    <span class="abs more" style="left:325px;top:150px">More</span>
    <h2 class="abs heading" style="left:24px;top:181px;width:621px">Our Products</h2>
    <p class="abs copy" style="left:24px;top:227px;width:630px">Lorem ipsum dolor sit amet, consectetur adipisicing elit, sed do eiusmod tempor incididunt ut labore et dolore magna aliqua. Ut enim ad minim veniam, quis nostrud exercitation ullamco laboris nisi ut aliquip ex ea commodo consequat. Duis aute irure dolor in reprehenderit in voluptate velit esse cillum dolore eu fugiat nulla pariatur. Excepteur sint occaecat cupidatat non proident, sunt in culpa qui officia deserunt mollit anim id est laborum.The standard chunk of Lorem Ipsum used since the 1500s is reproduced below for those interested......</p>
    <span class="abs more" style="left:325px;top:305px">More</span>
  </section>
  <h2 class="abs heading" style="left:230px;top:674px;width:615px">White Papers</h2>
  <section class="abs papers">
    <svg class="arrow" style="left:-9px;top:77px" width="24" height="24"><circle cx="12" cy="12" r="11" fill="#6a6a6a" stroke="#ccc" stroke-width="2"/><path d="M14 7l-5 5 5 5" stroke="#fff" stroke-width="2.5" fill="none"/></svg>
    <svg class="arrow" style="left:663px;top:77px" width="24" height="24"><circle cx="12" cy="12" r="11" fill="#6a6a6a" stroke="#ccc" stroke-width="2"/><path d="M10 7l5 5-5 5" stroke="#fff" stroke-width="2.5" fill="none"/></svg>
    <div class="paper" style="left:27px">Lorem ipsum dolor sit amet, consectetur adipisicing elit, sed do eiusmod tempor incididunt ut labore et dolore magna aliqua. Ut enim ad minim veniam, quis nostrud exercitation ullamco laboris nisiut aliquip ex ea commodo consequat. Duis aute irure dolor in reprehenderit in voluptate velit esse cillum dolore eu fugiat nulla pariatur. Excepteur sint occaecat cupidatat non proident, sunt in culpa qui officia deserunt mollit anim id .........<a class="dl">Download</a></div>
    <div class="abs divider"></div>
    <div class="paper" style="left:358px">Lorem ipsum dolor sit amet, consectetur adipisicing elit, sed do eiusmod tempor incididunt ut labore et dolore magna aliqua. Ut enim ad minim veniam, quis nostrud exercitation ullamco laboris nisiut aliquip ex ea commodo consequat. Duis aute irure dolor in reprehenderit in voluptate velit esse cillum dolore eu fugiat nulla pariatur. Excepteur sint occaecat cupidatat non proident, sunt in culpa qui officia deserunt mollit anim id .........<a class="dl" style="padding-right:0">Download</a></div>
  </section>
  <h2 class="abs heading" style="left:229px;top:893px;width:611px">Our Clients</h2>
  <section class="abs clients">
    <div class="client-row">
      <span>Prue</span><span>Ostrelan</span><span>Solvane</span><span>Brevik</span><span>Quorlit</span><span>GN</span><span>Haldmere</span><span>Castrevo</span><span>VONI</span><span>SALVEM</span>
    </div>
  </section>
  <div class="abs footline"></div>
  <div class="abs copyright"><span>C</span>Copyright information here</div>
  <div class="abs legal"><a href="#">Privacy Policy</a><a href="#">Terms of Use</a><a href="#">Sitemap</a></div>
  <div class="abs social"><span><i></i>Kinlo</span><span><i></i>Feedra</span><span><i></i>Twixel</span><span><i></i>Plusmo</span></div>
</div>
</body>
</html>
```